Velmora Ice Cream's brochure

We need a product brochure for our ice cream products. Our ice cream is certified organic made with coconut milk based. Therefore our ice cream range are not only dairy and gluten free but also sugar free. Basically our ice cream are healthy alternative to commercial ice cream out there that are full of sugar, preservatives, artificial colour/ flavour etc.
We would like to make a brochure which is not boring like reading a newspaper but something that is visual enough to reflect information about the health benefits and also are good for your wellbeing. People are very visual hence we would like a brochure that describes all information using visual images.

So here are the details we would like to include:
Dairy free
Gluten free
Fructose friendly (as sweetened with Rice Malt syrup)
Sugar Free
Certified Organic

Health benefits:
Rich in Medium Chain Fatty Acids (MCFAs)
Good source of essential fatty acids, iron, vitamins, and minerals
High in Lauric Acid
No artificial colours or flavours

Since our products are certified organic hence we would like to reflect organic feeling to the brochure.

Please email pella@velmora.com.au for any product images if required.

Target Market(s)

Health conscious people
Those who are intolerant to dairy, gluten and fructose
Young healthy females, mums with kids
People who are into organic product and healthy alternative

Industry/Entity Type

Health

Requirements
Must have
• Visual icons to show that our ice cream are:
• - Certified Organic
• - Dairy and Gluten Free
• - Sugar Free
• - Fructose Friendly (balance ratio of glucose : fructose); maybe to be creative we can use balance weight icon
• - Sweetened with Rice Malt Syrup
• Health benefits:
• Rich in Medium Chain Fatty Acids (MCFAs)
• Good source of essential fatty acids, iron, vitamins, and minerals
• High in Lauric Acid
• No artificial colours or flavours
Nice to have
• All 10 flavours - ice cream tubs
• But we are not sure how to fit all 10 ice cream flavours in a brochure. Maybe this is not practical given we might add more flavours by mid year or remove some of not so popular flavours.
• So we welcome any suggestion.

```html
<!DOCTYPE html>
<html lang="en">
<head>
<meta charset="utf-8">
<title>Velmora Ice Cream – Our Ice Creams</title>
<link rel="stylesheet" href="https://fonts.googleapis.com/css2?family=Amatic+SC:wght@400;700&display=swap">
<style>
  :root {
    --paper: #c8c6a6;
    --ink: #1f1d1a;
    --frame: #2f4a33;
    --badge: #2f4a33;
    --badge-mark: #e9e6cf;
    --tub-lid: #f4f2ea;
    --tub-blue: #9cc8e4;
    --tub-berry: #8b3a30;
    --tub-cream: #e9e4cb;
    --tub-coffee: #d6a233;
    --tub-hazel: #6a4230;
    --tub-mango: #ec8a2c;
    --tub-sesame: #2d8ed4;
    --tub-caramel: #ee8c30;
    --tub-honey: #e3a63d;
    --tub-coconut: #8cc43c;
  }
  * { margin: 0; padding: 0; box-sizing: border-box; }
  html, body { width: 1200px; height: 845px; overflow: hidden; background: var(--paper); }
  .brochure {
    position: relative;
    width: 1200px; height: 845px;
    background: var(--paper);
    color: var(--ink);
    font-family: "Amatic SC", cursive;
  }
  .frame {
    position: absolute;
    left: 39px; top: 36px; width: 1110px; height: 770px;
    border: 1.5px solid var(--frame);
  }
  .title {
    position: absolute;
    left: 74px; top: 62px;
    font-size: 100px; font-weight: 400; line-height: 1;
    letter-spacing: 4px;
    text-transform: uppercase;
  }
  .claims {
    position: absolute;
    left: 631px; top: 70px; width: 500px;
    list-style: none;
    font-size: 17px; line-height: 21px; font-weight: 700;
    text-transform: uppercase;
    letter-spacing: 0.3px;
  }
  .claim { display: inline; margin-right: 8px; white-space: normal; }
  .claim-icon {
    display: inline-block;
    width: 14px; height: 14px;
    margin-right: 4px;
    vertical-align: -2px;
  }
  .claims-heading { display: inline; margin-right: 6px; text-decoration: underline; }
  .divider {
    position: absolute;
    left: 594px; top: 203px; width: 1.5px; height: 568px;
    background: var(--frame);
  }
  .flavours {
    position: absolute;
    top: 184px;
    list-style: none;
  }
  .flavours--left { left: 73px; }
  .flavours--right { left: 632px; }
  .flavour {
    display: flex; align-items: center;
    height: 118px;
  }
  .tub {
    flex: none;
    width: 96px; height: 112px;
    margin-right: 12px;
    border-radius: 6px 6px 10px 10px;
    border-top: 16px solid var(--tub-lid);
  }
  .flavour-name {
    font-size: 62px; font-weight: 400; line-height: 60px;
    letter-spacing: 2px;
    text-transform: uppercase;
  }
  .tub--choc-coconut { background: linear-gradient(var(--tub-blue), #86b7d8); }
  .tub--choc-raspberry { background: linear-gradient(var(--tub-berry), #6f2c25); }
  .tub--vanilla-date { background: linear-gradient(var(--tub-cream), #d9d2b4); }
  .tub--iced-coffee { background: linear-gradient(var(--tub-coffee), #bf8c25); }
  .tub--hazelnut { background: linear-gradient(var(--tub-hazel), #553424); }
  .tub--mango { background: linear-gradient(var(--tub-mango), #d77520); }
  .tub--black-sesame { background: linear-gradient(var(--tub-sesame), #1f76b8); }
  .tub--salted-caramel { background: linear-gradient(var(--tub-caramel), #d67623); }
  .tub--caramel-honey { background: linear-gradient(var(--tub-honey), #cc8d2c); }
  .tub--naked-coconut { background: linear-gradient(var(--tub-coconut), #74ac2c); }
</style>
</head>
<body>
<main class="brochure">
  <svg width="0" height="0" style="position:absolute" aria-hidden="true">
    <symbol id="tick" viewBox="0 0 14 14">
      <circle cx="7" cy="7" r="7" fill="var(--badge)"/>
      <path d="M3.6 7.2 L6 9.6 L10.4 4.6" fill="none" stroke="var(--badge-mark)" stroke-width="1.8" stroke-linecap="round" stroke-linejoin="round"/>
    </symbol>
  </svg>

  <div class="frame"></div>

  <h1 class="title">Our Ice Creams</h1>

  <ul class="claims">
    <li class="claim"><svg class="claim-icon" aria-hidden="true"><use href="#tick"/></svg>Dairy free</li>
    <li class="claim"><svg class="claim-icon" aria-hidden="true"><use href="#tick"/></svg>Gluten free</li>
    <li class="claim"><svg class="claim-icon" aria-hidden="true"><use href="#tick"/></svg>Fructose friendly (as sweetened with rice malt syrup)</li>
    <li class="claim"><svg class="claim-icon" aria-hidden="true"><use href="#tick"/></svg>Sugar free</li>
    <li class="claim"><svg class="claim-icon" aria-hidden="true"><use href="#tick"/></svg>Certified organic</li>
    <li class="claims-heading">Health benefits:</li>
    <li class="claim"><svg class="claim-icon" aria-hidden="true"><use href="#tick"/></svg>Rich in medium chain fatty acids</li>
    <li class="claim"><svg class="claim-icon" aria-hidden="true"><use href="#tick"/></svg>Good source of essential fatty acids, iron, vitamins, and minerals</li>
    <li class="claim"><svg class="claim-icon" aria-hidden="true"><use href="#tick"/></svg>High in lauric acid</li>
    <li class="claim"><svg class="claim-icon" aria-hidden="true"><use href="#tick"/></svg>No artificial colours or flavours</li>
  </ul>

  <ul class="flavours flavours--left">
    <li class="flavour"><div class="tub tub--choc-coconut" role="img" aria-label="Velmora Choc Coconut ice cream tub"></div><span class="flavour-name">Choc Coconut</span></li>
    <li class="flavour"><div class="tub tub--choc-raspberry" role="img" aria-label="Velmora Choc Rasberry Ripple ice cream tub"></div><span class="flavour-name">Choc Rasberry Ripple</span></li>
    <li class="flavour"><div class="tub tub--vanilla-date" role="img" aria-label="Velmora Vanilla, Sticky Date and Pecan ice cream tub"></div><span class="flavour-name">Vanilla, Sticky<br>Date and Pecan</span></li>
    <li class="flavour"><div class="tub tub--iced-coffee" role="img" aria-label="Velmora Iced Coffee ice cream tub"></div><span class="flavour-name">Iced Coffee</span></li>
    <li class="flavour"><div class="tub tub--hazelnut" role="img" aria-label="Velmora Hazelnut ice cream tub"></div><span class="flavour-name">Hazelnut</span></li>
  </ul>

  <div class="divider"></div>

  <ul class="flavours flavours--right">
    <li class="flavour"><div class="tub tub--mango" role="img" aria-label="Velmora Mango ice cream tub"></div><span class="flavour-name">Mango</span></li>
    <li class="flavour"><div class="tub tub--black-sesame" role="img" aria-label="Velmora Black Sesame ice cream tub"></div><span class="flavour-name">Black Sesame</span></li>
    <li class="flavour"><div class="tub tub--salted-caramel" role="img" aria-label="Velmora Salted Caramel ice cream tub"></div><span class="flavour-name">Salted Caramel</span></li>
    <li class="flavour"><div class="tub tub--caramel-honey" role="img" aria-label="Velmora Caramel Honey Macadamia ice cream tub"></div><span class="flavour-name">Caramel Honey<br>Macadamia</span></li>
    <li class="flavour"><div class="tub tub--naked-coconut" role="img" aria-label="Velmora Naked Coconut ice cream tub"></div><span class="flavour-name">Naked Coconut</span></li>
  </ul>
</main>
</body>
</html>
```